Brochure and business Design Project

I need to designee brochures for my company and need material helps me to market my business.
I own a corporate housing company and accommodations services which is we rent out furnished apartment for short term lease 30 days or more and we provider many services for international patient who come to Houston Brightwater medical center for medical treatment , pleasure , business or visit we also provide help with limousine service airport pick ups , cleaning services , concierge service , car rental services , prepaid services , immigration stay extend service .
explain about services we provide and talk about our goal and the company, i need inviting colors we accommodating people like hotline and etc, my logo must be change to fit with new design, i do not want to copy and past what i have on my website or on what i sent i need better story and something to help me marking my hosting business

Target Market(s)

business material

Industry/Entity Type

Accommodation

Colors

Designer to choose colors to be used in the design.

Requirements
Must have
• explain about services we provide and talk about our goal and the company, i need inviting colors we accommodating people like hotline and etc, my logo must be change to fit with new design, i do not want to copy and past what i have on my website or on what i sent i need better story and something to help me marking my business . we accommodate patient from all over the planet who comes for medicl treatment at Brightwater medical center
Nice to have
• different langue's
Should not have
• any sexual , or religion signs

```html
<!DOCTYPE html>
<html lang="en">
<head>
<meta charset="utf-8">
<title>Our Services – Brochure Interior</title>
<link href="https://fonts.googleapis.com/css2?family=Open+Sans:wght@600;700&family=Tinos:wght@400;700&display=swap" rel="stylesheet">
<style>
  :root {
    --page-bg: #e9e9e9;
    --band-top: #6d8ea6;
    --band-bottom: #46647c;
    --panel-dark: #26313f;
    --panel-mid: #3b4c5d;
    --city-warm: #7a6450;
    --text-main: #ffffff;
    --text-soft: #dfe5ea;
    --accent: #e8185a;
    --rule: rgba(255,255,255,0.35);
    --icon-disc: rgba(20,28,38,0.55);
  }
  * { margin: 0; padding: 0; box-sizing: border-box; }
  html, body { width: 1200px; height: 916px; overflow: hidden; background: var(--page-bg); }
  .brochure {
    position: relative; width: 1200px; height: 916px; overflow: hidden;
    font-family: "Tinos", "Times New Roman", serif; color: var(--text-main);
  }
  .city-backdrop {
    position: absolute; inset: 0;
    background:
      radial-gradient(ellipse at 30% 70%, rgba(160,120,80,0.55), transparent 55%),
      radial-gradient(ellipse at 60% 40%, rgba(90,110,130,0.5), transparent 60%),
      linear-gradient(180deg, var(--panel-mid) 0%, var(--panel-dark) 45%, var(--city-warm) 100%);
  }
  .header-band {
    position: absolute; left: 0; top: 0; width: 1200px; height: 110px;
    background: linear-gradient(180deg, var(--band-top), var(--band-bottom));
    opacity: 0.92;
  }
  .fold { position: absolute; top: 0; width: 1px; height: 916px; background: rgba(0,0,0,0.35); box-shadow: 1px 0 0 rgba(255,255,255,0.12); }
  .fold.one { left: 400px; }
  .fold.two { left: 800px; }
  .section-title {
    position: absolute; top: 36px; left: 0; width: 800px; text-align: center;
    font-family: "Open Sans", Arial, sans-serif; font-weight: 700; font-size: 38px; letter-spacing: 1px;
  }
  .section-title .accent { color: var(--accent); }
  .gallery-title {
    position: absolute; top: 36px; left: 800px; width: 400px; text-align: center;
    font-family: "Open Sans", Arial, sans-serif; font-weight: 700; font-size: 38px; letter-spacing: 1px;
  }
  .service-column { position: absolute; top: 110px; width: 400px; }
  .service-column.left { left: 0; }
  .service-column.middle { left: 400px; }
  .service {
    display: flex; align-items: flex-start; gap: 22px;
    padding: 24px 26px 20px 30px; border-bottom: 1px solid var(--rule);
    background: rgba(30,40,52,0.35);
  }
  .service-column.left .service { height: 134px; }
  .service-column.middle .service { height: 120px; }
  .service-column.middle .service.general { height: 200px; }
  .service-icon {
    flex: none; width: 46px; height: 46px; border-radius: 50%;
    background: var(--icon-disc); display: flex; align-items: center; justify-content: center;
  }
  .service-icon svg { width: 26px; height: 26px; fill: none; stroke: #fff; stroke-width: 2; stroke-linecap: round; stroke-linejoin: round; }
  .service-name { font-weight: 700; font-size: 25px; line-height: 1.1; margin-bottom: 6px; }
  .service-detail { font-size: 16px; line-height: 1.3; color: var(--text-soft); }
  .service-detail small { font-size: 11px; }
  .gallery { position: absolute; top: 135px; left: 840px; width: 330px; }
  .gallery-photo { width: 330px; height: 170px; margin-bottom: 14px; box-shadow: 0 4px 10px rgba(0,0,0,0.4); }
  .photo-gym { background: linear-gradient(160deg, #e8e6e0, #b6a88f); }
  .photo-pool { background: linear-gradient(180deg, #6fa2cf 0%, #4f8a4a 55%, #2f5d7a 100%); }
  .photo-lounge { background: linear-gradient(160deg, #cfd2d4, #8b8f92 60%, #5a5d60); }
  .photo-bedroom { background: linear-gradient(160deg, #a9b6bd, #e7e2dc 55%, #8a6f6d); }
</style>
</head>
<body>
<main class="brochure">
  <div class="city-backdrop" role="img" aria-label="Blurred evening city skyline photo behind the services panels"></div>
  <div class="header-band"></div>
  <div class="fold one"></div>
  <div class="fold two"></div>

  <h1 class="section-title"><span class="accent">OUR</span> SERVICES</h1>
  <h2 class="gallery-title">GALLERY</h2>

  <section class="service-column left">
    <div class="service">
      <span class="service-icon"><svg viewBox="0 0 24 24"><path d="M3 9a13 13 0 0 1 18 0M6 12.5a8.5 8.5 0 0 1 12 0M9 16a4 4 0 0 1 6 0"/><circle cx="12" cy="19" r="0.8" fill="#fff"/></svg></span>
      <div><div class="service-name">Internet</div><p class="service-detail">WiFi is available in the hotel rooms<br>and is free of charge.</p></div>
    </div>
    <div class="service">
      <span class="service-icon"><svg viewBox="0 0 24 24"><path d="M4 15l2-5h12l2 5v3H4z"/><circle cx="8" cy="18" r="1.5"/><circle cx="16" cy="18" r="1.5"/></svg></span>
      <div><div class="service-name">Parking</div><p class="service-detail">Free private parking is available on<br>site (reservation is not needed).</p></div>
    </div>
    <div class="service">
      <span class="service-icon"><svg viewBox="0 0 24 24"><circle cx="12" cy="15" r="4"/><circle cx="6" cy="9" r="1.6"/><circle cx="10" cy="6" r="1.6"/><circle cx="14" cy="6" r="1.6"/><circle cx="18" cy="9" r="1.6"/></svg></span>
      <div><div class="service-name">Pets</div><p class="service-detail">Pets are allowed on request.<br>Charges may apply.</p></div>
    </div>
    <div class="service">
      <span class="service-icon"><svg viewBox="0 0 24 24"><path d="M3 14c2-2 4 2 6 0s4 2 6 0 4 2 6 0M3 19c2-2 4 2 6 0s4 2 6 0 4 2 6 0"/></svg></span>
      <div><div class="service-name">Pool</div><p class="service-detail">Outdoor Pool – FREE<br>Outdoor Pool (seasonal) – FREE</p></div>
    </div>
    <div class="service">
      <span class="service-icon"><svg viewBox="0 0 24 24"><path d="M8 3v18M5 3v5a3 3 0 0 0 6 0V3M16 21V3c2 1 3 4 3 8h-3"/></svg></span>
      <div><div class="service-name">Food &amp; Drink</div><p class="service-detail">BBQ Facilities</p></div>
    </div>
    <div class="service">
      <span class="service-icon"><svg viewBox="0 0 24 24"><path d="M4 11l8-7 8 7M6 9.5V20h12V9.5M10 20v-5h4v5"/></svg></span>
      <div><div class="service-name">Family Friendly</div><p class="service-detail">Family Rooms</p></div>
    </div>
  </section>

  <section class="service-column middle">
    <div class="service">
      <span class="service-icon"><svg viewBox="0 0 24 24"><path d="M12 4c3 3 3 9 0 13-3-4-3-10 0-13zM12 17c-4 0-7-2-8-6 3 0 6 2 8 6zM12 17c4 0 7-2 8-6-3 0-6 2-8 6z"/></svg></span>
      <div><div class="service-name">Spa &amp; Wellness</div><p class="service-detail">Fitness Center – FREE</p></div>
    </div>
    <div class="service">
      <span class="service-icon"><svg viewBox="0 0 24 24"><circle cx="12" cy="12" r="7"/><circle cx="12" cy="12" r="2.5"/></svg></span>
      <div><div class="service-name">Activities</div><p class="service-detail">Pool Table – FREE</p></div>
    </div>
    <div class="service">
      <span class="service-icon"><svg viewBox="0 0 24 24"><path d="M17 3l-6 9M8 12h6l3 9H5z"/></svg></span>
      <div><div class="service-name">Cleaning Services</div><p class="service-detail">Laundry</p></div>
    </div>
    <div class="service">
      <span class="service-icon"><svg viewBox="0 0 24 24"><rect x="5" y="4" width="14" height="13" rx="2"/><path d="M5 11h14"/><circle cx="8" cy="14" r="0.8"/><circle cx="16" cy="14" r="0.8"/><path d="M7 17v3M17 17v3"/></svg></span>
      <div><div class="service-name">Transportation</div><p class="service-detail">Airport Shuttle<br>Airport Shuttle <small>(additional charge)</small><br>Car Rental</p></div>
    </div>
    <div class="service general">
      <span class="service-icon"><svg viewBox="0 0 24 24"><circle cx="12" cy="12" r="9"/><path d="M12 11v6"/><circle cx="12" cy="7.5" r="0.8" fill="#fff"/></svg></span>
      <div><div class="service-name">General</div><p class="service-detail">Non-smoking Rooms<br>Air Conditioning – FREE<br>All Spaces Non-Smoking <small>(public and private)</small><br>Elevator<br>Heating<br>Grounds<br>Terrace</p></div>
    </div>
  </section>

  <section class="gallery">
    <div class="gallery-photo photo-gym" role="img" aria-label="Fitness room with exercise bikes"></div>
    <div class="gallery-photo photo-pool" role="img" aria-label="Resort lake with palm trees"></div>
    <div class="gallery-photo photo-lounge" role="img" aria-label="Living room with white sofas and city view"></div>
    <div class="gallery-photo photo-bedroom" role="img" aria-label="Bedroom with large bed and window view"></div>
  </section>
</main>
</body>
</html>
```